Letterhead to Prospective Clients

Create a letterhead (word & canva) that I will use to send letters to prospective clients and also include the Coralwood Estate Partners Logo, My Contact Details and Interchangeable "Suburb". Use the same font and colour pallete

Maris Dulworth | "Suburb" Specialist - Redlands & Surrounds
Mobile: 0417 862 095
Email: MD@CoralwoodEstatePartners.com.au

```html
<!DOCTYPE html>
<html lang="en">
<head>
<meta charset="UTF-8">
<title>Coralwood Estate Partners Letterhead</title>
<link rel="stylesheet" href="https://fonts.googleapis.com/css2?family=Poppins:wght@300;400;600&display=swap">
<style>
  :root {
    --backdrop: #aaaaaa;
    --paper: #ffffff;
    --navy: #001359;
    --gold: #d4a56b;
    --ink: #222222;
    --mist: #e4e4e4;
  }
  * { margin: 0; padding: 0; box-sizing: border-box; }
  html, body {
    width: 872px;
    height: 1200px;
    overflow: hidden;
    background: var(--backdrop);
    font-family: "Poppins", sans-serif;
  }
  .letterhead {
    position: absolute;
    left: 102px;
    top: 92px;
    width: 678px;
    height: 1017px;
    background: var(--paper);
    overflow: hidden;
  }
  .brand-name {
    position: absolute;
    left: 29px;
    top: 20px;
    color: var(--gold);
    font-weight: 300;
    line-height: 1;
    text-align: center;
  }
  .brand-name .primary {
    display: block;
    font-size: 26px;
    letter-spacing: 2px;
  }
  .brand-name .secondary {
    display: block;
    font-size: 9.5px;
    letter-spacing: 3.2px;
    margin-top: 5px;
  }
  .header-rule {
    position: absolute;
    left: 159px;
    right: 0;
    top: 51px;
    height: 1px;
    background: var(--gold);
  }
  .backdrop-name {
    position: absolute;
    left: 340px;
    top: 490px;
    transform: translate(-50%, -50%) rotate(-26deg);
    color: var(--mist);
    font-weight: 300;
    font-size: 78px;
    letter-spacing: 6px;
    white-space: nowrap;
  }
  .signature-bar {
    position: absolute;
    left: 0;
    top: 916px;
    width: 12px;
    height: 88px;
    background: var(--navy);
  }
  .contact-block {
    position: absolute;
    left: 29px;
    top: 912px;
    color: var(--ink);
    font-size: 13.5px;
    line-height: 1.4;
  }
  .contact-name {
    color: var(--navy);
    font-weight: 600;
    font-size: 16.5px;
    line-height: 1.3;
  }
  .contact-role { margin-bottom: 13px; }
  .contact-label { color: var(--navy); font-weight: 600; }
  .contact-line { line-height: 1.38; }
</style>
</head>
<body>
  <main class="letterhead">
    <div class="brand-name">
      <span class="primary">CORALWOOD</span>
      <span class="secondary">ESTATE PARTNERS</span>
    </div>
    <div class="header-rule"></div>

    <div class="backdrop-name" aria-hidden="true">CORALWOOD</div>

    <div class="signature-bar"></div>
    <section class="contact-block">
      <p class="contact-name">Maris Dulworth</p>
      <p class="contact-role">"Suburb" Specialist Redlands &amp; Surrounds</p>
      <p class="contact-line"><span class="contact-label">P:</span> 0417 862 095</p>
      <p class="contact-line"><span class="contact-label">E:</span> MD@CoralwoodEstatePartners.com.au</p>
    </section>
  </main>
</body>
</html>
```